Quill And Ferry Business Card

I need a business card designed around my logo (which was designed here on Sketch Forum!)

Target Market(s)

Professional Businesses

Industry/Entity Type

Business

Requirements
Must have
• Details that must be on the business card:

Renata Ovalle
Director
0491 253 608
renata@quillandferry.com.au
www.quillandferry.com.au
PO Box 4720 Fitzroy North Vic 3068

```html
<!DOCTYPE html>
<html lang="en">
<head>
<meta charset="utf-8">
<title>Quill And Ferry Business Card</title>
<link rel="stylesheet" href="https://fonts.googleapis.com/css2?family=Cinzel:wght@400;600&family=Lato:wght@400;700&display=swap">
<style>
  :root {
    --stage: #ece8e3;
    --card-red: #d61f2c;
    --card-red-deep: #b5121d;
    --ink-white: #ffffff;
    --tint-white: rgba(255, 255, 255, 0.82);
    --shadow: rgba(60, 20, 20, 0.25);
  }
  * { box-sizing: border-box; margin: 0; padding: 0; }
  html, body {
    width: 1200px; height: 1023px; overflow: hidden;
    background: var(--stage);
  }
  .canvas {
    width: 1200px; height: 1023px;
    display: flex; flex-direction: column;
    align-items: center; justify-content: center; gap: 70px;
  }
  .card {
    position: relative;
    width: 560px; height: 320px;
    background: linear-gradient(160deg, var(--card-red) 0%, var(--card-red-deep) 100%);
    border-radius: 4px;
    box-shadow: 0 14px 30px var(--shadow);
    color: var(--ink-white);
    overflow: hidden;
  }
  .corner-pattern {
    position: absolute; width: 70px; height: 44px;
    background: linear-gradient(135deg, rgba(255,255,255,0.55), rgba(255,255,255,0.25));
    border-radius: 2px;
  }
  .corner-pattern.top-left { top: 28px; left: 30px; }
  .corner-pattern.top-right { top: 28px; right: 30px; }
  .corner-pattern.bottom-left { bottom: 28px; left: 30px; }
  .corner-pattern.bottom-right { bottom: 28px; right: 30px; }

  .brand {
    position: absolute; inset: 0;
    display: flex; align-items: center; justify-content: center; gap: 18px;
  }
  .brand-mark {
    width: 46px; height: 46px; border-radius: 50%;
    background: var(--ink-white);
  }
  .brand-text { display: flex; flex-direction: column; }
  .brand-name {
    font-family: "Cinzel", serif; font-weight: 600;
    font-size: 34px; letter-spacing: 1px; line-height: 1.1;
  }
  .brand-tagline {
    font-family: "Cinzel", serif; font-weight: 400;
    font-size: 15px; letter-spacing: 2.4px; margin-top: 2px;
  }

  .contact {
    position: absolute; left: 48px; top: 50%;
    transform: translateY(-50%);
  }
  .contact-name {
    font-family: "Cinzel", serif; font-weight: 600;
    font-size: 26px; letter-spacing: 1px;
  }
  .contact-role {
    font-family: "Lato", sans-serif; font-size: 14px;
    letter-spacing: 2px; text-transform: uppercase;
    color: var(--tint-white); margin: 4px 0 22px;
  }
  .contact-list { list-style: none; }
  .contact-item {
    display: flex; align-items: center; gap: 12px;
    font-family: "Lato", sans-serif; font-size: 15px;
    margin-bottom: 9px;
  }
  .contact-badge {
    width: 20px; height: 20px; border-radius: 3px;
    background: var(--ink-white); color: var(--card-red);
    font-family: "Lato", sans-serif; font-weight: 700; font-size: 12px;
    display: flex; align-items: center; justify-content: center;
  }
</style>
</head>
<body>
<main class="canvas">
  <section class="card card-front">
    <div class="corner-pattern top-left" role="img" aria-label="Small decorative pattern of white squares"></div>
    <div class="corner-pattern top-right" role="img" aria-label="Small decorative pattern of white squares"></div>
    <div class="corner-pattern bottom-left" role="img" aria-label="Small decorative pattern of white squares"></div>
    <div class="corner-pattern bottom-right" role="img" aria-label="Small decorative pattern of white squares"></div>
    <div class="brand">
      <span class="brand-mark"></span>
      <div class="brand-text">
        <span class="brand-name">QUILL AND FERRY</span>
        <span class="brand-tagline">BOOKKEEPING MADE EASY</span>
      </div>
    </div>
  </section>

  <section class="card card-back">
    <div class="contact">
      <p class="contact-name">Renata Ovalle</p>
      <p class="contact-role">Director</p>
      <ul class="contact-list">
        <li class="contact-item"><span class="contact-badge">P</span>0491 253 608</li>
        <li class="contact-item"><span class="contact-badge">E</span>renata@quillandferry.com.au</li>
        <li class="contact-item"><span class="contact-badge">W</span>www.quillandferry.com.au</li>
        <li class="contact-item"><span class="contact-badge">A</span>PO Box 4720 Fitzroy North Vic 3068</li>
      </ul>
    </div>
  </section>
</main>
</body>
</html>
```